Bref créative
Logo for a homebuyer business
Brightkey Dwellings Homebuyers
Use same font as used in my logo
Miriam Colby
Co-Owner
xxxxx
BrightKeyDwellings@mailbox-example.net
BrightKeyDwellings.example

```html
<!DOCTYPE html>
<html lang="en">
<head>
<meta charset="utf-8">
<title>Brightkey Dwellings Homebuyers – Business Cards</title>
<link rel="stylesheet" href="https://fonts.googleapis.com/css2?family=Open+Sans:wght@400;600;700&display=swap">
<style>
  :root {
    --backdrop: #d9dadc;
    --card-white: #ffffff;
    --royal-blue: #2a3a9e;
    --navy: #1f2a6e;
    --bronze: #8a5a2b;
    --ink-soft: #3a3f5c;
  }
  * { margin: 0; padding: 0; box-sizing: border-box; }
  html, body { width: 1200px; height: 895px; overflow: hidden; }
  body {
    background: var(--backdrop);
    font-family: "Open Sans", Arial, sans-serif;
    display: flex;
    flex-direction: column;
    align-items: center;
    justify-content: center;
    gap: 40px;
  }
  .card {
    position: relative;
    width: 700px;
    height: 400px;
    background: var(--card-white);
    box-shadow: 0 6px 18px rgba(0,0,0,0.18);
    overflow: hidden;
  }
  .card-wave { position: absolute; inset: 0; }
  .contact-block {
    position: absolute;
    left: 48px;
    top: 42px;
    color: var(--card-white);
  }
  .person-name { font-size: 24px; font-weight: 600; letter-spacing: 0.3px; }
  .person-role { font-size: 15px; margin-top: 2px; opacity: 0.95; }
  .contact-list { list-style: none; margin-top: 70px; }
  .contact-list li {
    display: flex; align-items: center; gap: 9px;
    font-size: 12.5px; line-height: 1; margin-bottom: 9px;
  }
  .contact-icon { width: 16px; height: 16px; flex: none; }
  .brand-lockup {
    position: absolute;
    display: flex; align-items: center; gap: 12px;
    color: var(--navy);
    font-weight: 600;
    text-transform: uppercase;
    letter-spacing: 1.5px;
    line-height: 1.15;
  }
  .brand-mark { width: 14px; height: 14px; background: var(--bronze); flex: none; }
  .contact-card .brand-lockup { left: 440px; top: 170px; font-size: 19px; }
  .logo-card .brand-lockup { left: 50%; top: 140px; transform: translateX(-50%); font-size: 26px; }
  .logo-card .site-url {
    position: absolute; left: 0; right: 0; top: 268px;
    text-align: center; font-size: 15px; letter-spacing: 1px;
    color: var(--ink-soft);
  }
</style>
</head>
<body>

  <section class="card logo-card">
    <div class="brand-lockup"><span class="brand-mark"></span><span>Brightkey Dwellings<br>Homebuyers</span></div>
    <p class="site-url">www.BrightKeyDwellings.example</p>
  </section>

  <section class="card contact-card">
    <svg class="card-wave" viewBox="0 0 700 400" width="700" height="400" aria-hidden="true">
      <path d="M0,0 H420 C340,60 300,140 318,220 C336,300 300,360 240,400 H0 Z" fill="var(--royal-blue)"/>
      <path d="M426,0 C346,60 308,140 326,220 C344,300 308,360 250,400" fill="none" stroke="var(--bronze)" stroke-width="5"/>
    </svg>

    <div class="contact-block">
      <h1 class="person-name">Miriam Colby</h1>
      <p class="person-role">Co-Owner</p>
      <ul class="contact-list">
        <li>
          <svg class="contact-icon" viewBox="0 0 16 16"><circle cx="8" cy="8" r="8" fill="#fff"/><path d="M5.2 4.5l1.4-.3.8 1.8-.9.7a5 5 0 0 0 2.8 2.8l.7-.9 1.8.8-.3 1.4c-3.3.3-6.6-3-6.3-6.3z" fill="var(--royal-blue)"/></svg>
          555-014-7890
        </li>
        <li>
          <svg class="contact-icon" viewBox="0 0 16 16"><circle cx="8" cy="8" r="8" fill="#fff"/><rect x="5.5" y="3.5" width="5" height="9" rx="1" fill="var(--royal-blue)"/></svg>
          (555) 014-2297
        </li>
        <li>
          <svg class="contact-icon" viewBox="0 0 16 16"><circle cx="8" cy="8" r="8" fill="#fff"/><rect x="4" y="5" width="8" height="6" fill="var(--royal-blue)"/><path d="M4 5l4 3.2L12 5" fill="none" stroke="#fff" stroke-width="0.9"/></svg>
          BrightKeyDwellings@mailbox-example.net
        </li>
        <li>
          <svg class="contact-icon" viewBox="0 0 16 16"><circle cx="8" cy="8" r="8" fill="#fff"/><circle cx="8" cy="8" r="4" fill="none" stroke="var(--royal-blue)" stroke-width="1"/><path d="M4 8h8M8 4c-2 2.4-2 5.6 0 8M8 4c2 2.4 2 5.6 0 8" fill="none" stroke="var(--royal-blue)" stroke-width="0.8"/></svg>
          www.BrightKeyDwellings.example
        </li>
      </ul>
    </div>

    <div class="brand-lockup"><span class="brand-mark"></span><span>Brightkey Dwellings<br>Homebuyers</span></div>
  </section>

</body>
</html>
```